Brochure to promote Wayplacard.com which turns RVs into Billboards

Sample Text to choose from for Wayplacard Brochure
π’ Wayplacard | RV Advertising Tagline: Your Brand. Your Message. Coast to Coast.
π The Big Opportunity
Why RV Advertising?
Mobile billboards go where people go
High visibility on highways, campgrounds, festivals
Extended exposure (parked RVs = static billboards)
Fueled by rising popularity of RV vacations and road travel
π Who Sees Your Ads?
Demographics: Families, retirees, outdoor enthusiasts, festival goers
Geographic Reach:
Avg. 3,500 daily impressions per RV (~105,000/month)
Routes cover highways, national parks, big events
Locations: Campgrounds, concerts, fairs, sports venues, tourist hubs
π Our Vehicles
Single RV:
Example: Class A RV, 40 ft.
Wrap space: full sides + rear = thousands of sq. in. of branding
Fleet Option:
10+ RVs across U.S. regions
Nationwide reach and simultaneous event coverage
π¨ Advertising Options
Full wrap (premium visibility)
Partial wrap (budget-friendly)
Removable event banners
Custom packages (festivals, sports events, seasonal)
π Visibility & Traffic Stats
Highway traffic counts: Tens of thousands daily
Event attendance: 10kβ100k+ visitors
Estimated impressions:
Single RV: ~1.26M/year
Fleet (10 RVs): ~12.6M/year
Optional GPS Tracking: Prove exposure with data
π° Cost & Value
Competitive CPM Rates:
Static billboards: $2β$10 CPM
Mobile OOH (vehicles): $3β$15 CPM
RV Advertising: $5β$12 CPM
Sample Pricing (Mid CPM $8):
Single RV, Monthly: $840
Single RV, Annual: $10,080
Single Event (per day): $200
Fleet of 10, Monthly: $8,400
Fleet of 10, Annual: $100,800
π Multi-year contracts available (10β15% discount)
π Past Clients / Conceptual Examples
Mockups of branded RVs (progressive campaigns)
Ideal for travel, outdoor, food & beverage, tech, and lifestyle brands
π Call to Action
βLetβs put your brand on the road.β
π§ Email: gerald@wayplacard.example
βοΈ Phone: (555) 417-9263
π Website: www.wayplacard.example
πΈ Instagram: @Wayplacard
β
Bottom Line: RV advertising delivers mobile reach, high impressions, and eventβbased visibility at a competitive CPM. Perfect for brands that want to travel directly into the heart of their audience.

```html
<!DOCTYPE html>
<html lang="en">
<head>
<meta charset="utf-8">
<title>Wayplacard RV Advertising Brochure</title>
<link rel="stylesheet" href="https://fonts.googleapis.com/css2?family=Montserrat:wght@500;700;800;900&family=Open+Sans:wght@400;600;700&display=swap">
<style>
  :root{
    --navy:#15163a;
    --navy-deep:#0d0e29;
    --purple:#6b1fd1;
    --violet:#8a3cf0;
    --magenta:#c43cf5;
    --lavender:#efe8fb;
    --ink:#1d1d2b;
    --muted:#55566a;
    --paper:#ffffff;
    --canvas:#f1f1f4;
  }
  *{box-sizing:border-box;margin:0;padding:0}
  html,body{width:851px;height:1200px;overflow:hidden;background:var(--canvas)}
  body{position:relative;font-family:'Open Sans',sans-serif;color:var(--ink)}
  .abs{position:absolute}
  h2,h3,h4{font-family:'Montserrat',sans-serif}

  /* ---------- outside spread ---------- */
  .cover{left:28px;top:20px;width:795px;height:272px;background:var(--navy);overflow:hidden;box-shadow:0 2px 8px rgba(0,0,0,.18)}
  .cover-back{left:0;top:0;width:265px;height:272px;background:linear-gradient(180deg,#23244d 0%,var(--navy-deep) 100%)}
  .back-photo{left:0;top:0;width:265px;height:120px;background:linear-gradient(180deg,#3a3360 0%,#1a1a3d 100%);opacity:.7}
  .brand-back{left:22px;top:118px;font-family:'Montserrat',sans-serif;font-weight:800;font-size:15px;letter-spacing:2px;color:#fff;text-transform:uppercase}
  .cta{left:22px;top:142px;padding:5px 10px;background:var(--purple);color:#fff;font-size:9px;font-weight:600}
  .contacts{left:22px;top:178px;list-style:none;font-size:7.5px;color:#dcdcf0;line-height:14px}
  .contacts li{display:flex;align-items:center;gap:6px}
  .contacts svg{width:8px;height:8px;fill:var(--magenta)}
  .bottom-line{left:140px;top:176px;width:115px;font-size:7px;line-height:10.5px;color:#c9c9e0}
  .cover-front{left:265px;top:0;width:530px;height:272px;background:linear-gradient(120deg,#20134a 0%,#3b1373 55%,#5b1aa6 100%)}
  .front-photo{left:170px;top:90px;width:350px;height:175px;border-radius:4px;background:radial-gradient(ellipse at 55% 55%,#4aa0ff 0%,#7a2be0 40%,#2a0f57 80%)}
  .brand-front{left:22px;top:20px;font-family:'Montserrat',sans-serif;font-weight:800;font-size:11px;letter-spacing:2px;color:#fff;text-transform:uppercase}
  .headline{left:200px;top:22px;text-align:right;width:320px}
  .headline h1{font-family:'Montserrat',sans-serif;font-weight:900;font-size:26px;color:#fff;line-height:1;white-space:nowrap}
  .headline p{font-family:'Montserrat',sans-serif;font-weight:700;font-size:12px;color:var(--magenta);line-height:15px;margin-top:4px}
  .headline p span{color:#fff}

  /* ---------- inside spread ---------- */
  .inside{left:28px;top:306px;width:795px;height:876px;background:var(--paper);overflow:hidden;box-shadow:0 2px 8px rgba(0,0,0,.14)}
  .topbar{left:0;top:0;width:795px;height:6px;background:linear-gradient(90deg,var(--purple),var(--magenta))}
  .section-title{font-weight:800;font-size:20px;color:var(--navy);left:18px;top:26px}
  .kicker{font-family:'Montserrat',sans-serif;font-weight:800;font-size:14px;color:var(--navy);text-transform:uppercase;line-height:16px}
  .kicker em{font-style:normal;color:var(--purple)}
  .copy{font-size:8.5px;line-height:12.5px;color:var(--muted)}
  .copy strong{color:var(--ink)}
  .copy ul{list-style:none}
  .copy li{margin-bottom:5px}

  .why{left:18px;top:66px;width:210px}
  .why .copy{margin-top:8px}
  .vehicles{left:18px;top:276px;width:210px}
  .vehicles .copy{margin-top:8px}

  .who{left:232px;top:52px;width:168px;height:160px;background:var(--navy);color:#fff;padding:14px}
  .who h3{font-size:15px;font-weight:800;line-height:18px}
  .who h4{font-size:9px;color:var(--magenta);margin-top:8px;font-weight:700}
  .who ul{list-style:none;margin-top:6px;font-size:9px;line-height:14px}
  .who li::before{content:"";display:inline-block;width:5px;height:5px;background:var(--magenta);margin-right:6px;vertical-align:middle}
  .geo-head{left:232px;top:222px;width:168px;background:var(--purple);color:#fff;padding:8px 12px;font-family:'Montserrat',sans-serif;font-weight:800;font-size:13px;line-height:15px}
  .geo{left:236px;top:272px;width:160px}

  .options{left:408px;top:18px;width:158px;height:200px;background:var(--lavender);padding:12px}
  .options .kicker{font-size:12px;line-height:14px}
  .options .copy{margin-top:8px}
  .stats{left:578px;top:18px;width:205px}
  .stats .kicker{font-size:12px;line-height:14px}
  .stats .copy{margin-top:6px}
  .impressions{left:578px;top:96px;width:205px;background:var(--lavender);padding:8px 10px}
  .impressions h4{font-size:9px;color:var(--navy);margin-bottom:4px}

  .truck-photo{left:408px;top:226px;width:375px;height:135px;background:linear-gradient(135deg,#cfd6e4 0%,#8fa1bd 50%,#4a5b7a 100%)}
  .cost{left:560px;top:268px;width:235px;height:84px;background:var(--purple);color:#fff;padding:14px 16px}
  .cost h3{font-weight:900;font-size:20px;line-height:22px}
  .cost p{font-family:'Montserrat',sans-serif;font-weight:700;font-size:12px;margin-top:2px}

  .pricing{left:395px;top:380px;width:390px;display:grid;grid-template-columns:repeat(3,1fr);row-gap:12px;column-gap:10px}
  .price{border-top:2px solid var(--purple);padding:8px 0;text-align:center}
  .price b{display:block;font-family:'Montserrat',sans-serif;font-weight:800;font-size:15px;line-height:18px;color:var(--navy)}
  .price span{display:block;font-size:8.5px;line-height:11px;color:var(--muted);margin-top:3px}
  .price.feature{background:var(--navy);border-top-color:var(--magenta)}
  .price.feature b{color:#fff}
  .price.feature span{color:#d5d5ee}

  .rv-photo{left:0;top:500px;width:385px;height:250px;background:linear-gradient(160deg,#e8ecf3 0%,#b9c3d4 55%,#7d8aa3 100%)}
  .fleet{left:18px;top:540px;width:150px;background:var(--purple);color:#fff;padding:12px}
  .fleet h3{font-size:14px;font-weight:800}
  .fleet p{font-size:8.5px;line-height:12px;margin-top:6px}
  .fleet strong{display:block;font-size:10px}

  .discount{left:395px;top:620px;width:390px;background:var(--lavender);padding:12px 14px}
  .discount .copy{color:var(--ink)}
  .examples{left:395px;top:676px;width:390px}
  .examples .copy{margin-top:6px}
  .footer{left:0;top:770px;width:795px;height:106px;background:var(--navy);color:#fff;padding:22px 24px;display:flex;justify-content:space-between;align-items:center}
  .footer h3{font-size:18px;font-weight:800}
  .footer h3 span{color:var(--magenta)}
  .footer ul{list-style:none;font-size:9px;line-height:15px;color:#dcdcf0;text-align:right}
</style>
</head>
<body>

<section class="cover abs">
  <div class="cover-back abs">
    <div class="back-photo abs" role="img" aria-label="Night photo of a parked RV"></div>
    <div class="brand-back abs">Wayplacard</div>
    <div class="cta abs">Let's put your brand on the road</div>
    <ul class="contacts abs">
      <li><svg viewBox="0 0 10 10"><path d="M2 0h2l1 3-1.5 1a6 6 0 0 0 2.5 2.5L7 5l3 1v2a2 2 0 0 1-2 2A8 8 0 0 1 0 2a2 2 0 0 1 2-2z"/></svg>(555) 417-9263</li>
      <li><svg viewBox="0 0 10 10"><path d="M0 2h10v6H0z M0 2l5 3 5-3" /></svg>gerald@wayplacard.example</li>
      <li><svg viewBox="0 0 10 10"><circle cx="5" cy="5" r="5"/></svg>www.wayplacard.example</li>
      <li><svg viewBox="0 0 10 10"><rect width="10" height="10" rx="2"/></svg>@Wayplacard</li>
    </ul>
    <p class="bottom-line abs">RV advertising delivers mobile reach, high impressions, and event-based visibility at a competitive CPM. Perfect for brands that want to travel directly into the heart of their audience.</p>
  </div>
  <div class="cover-front abs">
    <div class="front-photo abs" role="img" aria-label="RV with a glowing full advertising wrap at night"></div>
    <div class="brand-front abs">Wayplacard</div>
    <div class="headline abs">
      <h1>RV ADVERTISING</h1>
      <p>Your <span>Brand.</span><br>Your <span>Message.</span><br>Coast to Coast</p>
    </div>
  </div>
</section>

<section class="inside abs">
  <div class="topbar abs"></div>
  <h2 class="section-title abs">The Big Opportunity</h2>

  <div class="why abs">
    <h3 class="kicker">Why RV <em>Advertising?</em></h3>
    <div class="copy"><ul>
      <li>Mobile billboards go where people go</li>
      <li>High visibility on highways, campgrounds, festivals</li>
      <li><strong>Extended exposure</strong><br>(parked RVs = static billboards)</li>
      <li>Fueled by rising popularity of RV vacations and road travel</li>
    </ul></div>
  </div>

  <div class="vehicles abs">
    <h3 class="kicker">Our <em>Vehicles</em></h3>
    <div class="copy"><ul>
      <li><strong>Single RV</strong><br>Example: Class A RV, 40 ft.</li>
      <li><strong>Wrap Space</strong><br>Full sides + rear = thousands of sq. in. of branding</li>
    </ul></div>
  </div>

  <div class="who abs">
    <h3>Who Sees Your Ads?</h3>
    <h4>Demographics</h4>
    <ul><li>Families</li><li>Retirees</li><li>Outdoor Enthusiasts</li><li>Festival Goers</li></ul>
  </div>
  <div class="geo-head abs">GEOGRAPHIC<br>REACH</div>
  <div class="geo abs copy"><ul>
    <li>Avg. 3,500 daily impressions per RV (~105,000/month)</li>
    <li>Routes cover highways, national parks, big events</li>
    <li><strong>Locations</strong><br>Campgrounds, concerts, fairs, sports venues, tourist hubs</li>
  </ul></div>

  <div class="options abs">
    <h3 class="kicker">Advertising Options</h3>
    <div class="copy"><ul>
      <li>Full wrap (premium visibility)</li>
      <li>Partial wrap (budget-friendly)</li>
      <li>Removable event banners</li>
      <li>Custom packages (festivals, sports events, seasonal)</li>
    </ul></div>
  </div>

  <div class="stats abs">
    <h3 class="kicker">Visibility &amp; Traffic Stats</h3>
    <div class="copy"><ul>
      <li>Highway traffic counts: Tens of thousands daily</li>
      <li>Event attendance: 10k–100k+ visitors</li>
    </ul></div>
  </div>
  <div class="impressions abs copy">
    <h4>Estimated Impressions</h4>
    <ul>
      <li>Single RV: ~1.26M/year</li>
      <li>Fleet (10 RVs): ~12.6M/year</li>
      <li><strong>Optional GPS Tracking</strong><br>Prove exposure with data</li>
    </ul>
  </div>

  <div class="truck-photo abs" role="img" aria-label="Wrapped RV parked at an outdoor event"></div>
  <div class="cost abs">
    <h3>COST &amp; VALUE</h3>
    <p>Competitive CPM Rates</p>
  </div>

  <div class="pricing abs">
    <div class="price"><b>$2–$10</b><span>Static<br>Billboards</span></div>
    <div class="price"><b>$3–$15</b><span>Mobile OOH<br>(vehicles)</span></div>
    <div class="price"><b>$5–$12</b><span>RV<br>Advertising</span></div>
    <div class="price"><b>$840</b><span>Single RV<br>Monthly</span></div>
    <div class="price"><b>$10,080</b><span>Single RV<br>Annual</span></div>
    <div class="price"><b>$200</b><span>Single Event<br>(per day)</span></div>
    <div class="price feature"><b>MID CPM $8</b><span>Sample<br>Pricing</span></div>
    <div class="price"><b>$8,400</b><span>Fleet of 10<br>Monthly</span></div>
    <div class="price"><b>$100,800</b><span>Fleet of 10<br>Annual</span></div>
  </div>

  <div class="rv-photo abs" role="img" aria-label="White Class C RV on the road with branded wrap"></div>
  <div class="fleet abs">
    <h3>FLEET OPTIONS</h3>
    <p><strong>10+ RVs</strong>across U.S. regions</p>
    <p><strong>Nationwide Reach</strong>&amp; simultaneous event coverage</p>
  </div>

  <div class="discount abs copy"><strong>Multi-year contracts available</strong> — save 10–15% with long-term campaigns.</div>
  <div class="examples abs">
    <h3 class="kicker">Conceptual <em>Examples</em></h3>
    <div class="copy"><ul>
      <li>Mockups of branded RVs for progressive campaigns</li>
      <li>Ideal for travel, outdoor, food &amp; beverage, tech, and lifestyle brands</li>
    </ul></div>
  </div>

  <div class="footer abs">
    <h3>Let's put your brand <span>on the road.</span></h3>
    <ul>
      <li>gerald@wayplacard.example</li>
      <li>(555) 417-9263</li>
      <li>www.wayplacard.example · @Wayplacard</li>
    </ul>
  </div>
</section>

</body>
</html>
```